Tallpine Facility Upkeep Systems

I need a full website built that must work on destkop and mobile. I have the logo's and will upload them however some stock industrial photos will be required. I will be hosting it on wix/godaddy for use with dynamics 365. Pretty simple requirements:

*Splash page
*What We Do
*How We do it
*Who Are We?
*Software
*Partnerships
*Contact: Includes twitter/insta and email/addy/phone

The site should be more scroll oriented with fewer tabs to allow for a improved mobile experience.
We're also looking for ways to improve our inbound marketing and would want to include various areas to get in touch /or collect their info. Look to www.kelnarova.com as an example of inbound marketing.
Images should be representative of the verticals we're focused on.

I have most of the content.

Target Market(s)

Asset intensive industries: Mining, Oil and Gas, Forest Products and Manufacturing.

Industry/Entity Type

Asset Management

Coding

Coded - Design and coding required

Number of Pages Required

5+ page

Font styles to use
Sans Serif

Requirements
Must have
• Must be easy to view and navigate on mobile and desktop.
Nice to have
• Employee/Customer portal.
Should not have
• Anything that will not display well in a mobile environment.

```html
<!DOCTYPE html>
<html lang="en">
<head>
<meta charset="utf-8">
<title>Tallpine Facility Upkeep Systems</title>
<link href="https://fonts.googleapis.com/css2?family=Montserrat:wght@300;400;500;600&display=swap" rel="stylesheet">
<style>
  :root {
    --navy: #1b2150;
    --green: #6a9a1f;
    --panel: #f0f0f0;
    --grey-text: #8a8a8a;
    --line: #c8c8c8;
    --teal: #66cdca;
    --mint: #64cf96;
    --lavender: #9b9bcc;
    --yellow: #ffcb2f;
    --orange: #ff9c33;
    --coral: #ff6633;
  }
  * { box-sizing: border-box; margin: 0; padding: 0; }
  html, body { width: 1200px; height: 2400px; overflow: hidden; background: #fff; }
  body { font-family: "Montserrat", Arial, sans-serif; color: var(--navy); position: relative; }

  .site-header { position: absolute; top: 30px; left: 0; width: 1200px; height: 50px; }
  .brand { position: absolute; left: 338px; top: 8px; width: 252px; text-align: center; }
  .brand-name { font-size: 30px; font-weight: 400; letter-spacing: 1px; color: var(--navy); line-height: 34px; display: block; }
  .menu-toggle { position: absolute; left: 816px; top: 13px; width: 36px; height: 24px; }
  .menu-toggle span { display: block; height: 2px; background: var(--navy); margin-bottom: 9px; }

  .hero { position: absolute; left: 296px; top: 110px; width: 608px; height: 536px; background: var(--panel); }
  .hero-art { position: absolute; left: 248px; top: 34px; width: 228px; height: 200px; border-radius: 8px;
    background: linear-gradient(135deg, #d9dde3 0%, #e8e3cf 60%, #f6dc72 100%); }
  .hero-title { position: absolute; top: 258px; width: 100%; text-align: center; font-size: 32px; font-weight: 500; letter-spacing: 1.5px; line-height: 40px; }
  .btn-learn { position: absolute; left: 224px; top: 376px; width: 138px; height: 45px; background: var(--green); color: #fff; border-radius: 5px; font-size: 17px; font-weight: 400; display: flex; align-items: center; justify-content: center; }
  .hero-edge { position: absolute; left: 0; top: 440px; }

  .drivers-intro { position: absolute; top: 658px; left: 296px; width: 608px; text-align: center; }
  .drivers-title { font-size: 32px; font-weight: 600; letter-spacing: 1px; line-height: 40px; }
  .drivers-text { margin-top: 14px; font-size: 17px; line-height: 30px; color: #333; font-weight: 400; }

  .driver-list { position: absolute; top: 811px; left: 312px; width: 568px; display: flex; flex-direction: column; gap: 13px; list-style: none; }
  .driver { height: 136px; border-radius: 4px; display: flex; align-items: center; color: #fff; }
  .driver-icon { width: 80px; height: 80px; margin-left: 38px; flex: none; border-radius: 10px; background: rgba(255,255,255,0.28); }
  .driver-label { margin-left: 30px; font-size: 23px; font-weight: 500; letter-spacing: 1px; line-height: 31px; text-transform: uppercase; }
  .driver--planned { background: var(--teal); }
  .driver--safety { background: var(--mint); }
  .driver--savings { background: var(--lavender); }
  .driver--uptime { background: var(--yellow); }
  .driver--assets { background: var(--orange); }
  .driver--inventory { background: var(--coral); }

  .site-footer { position: absolute; left: 296px; top: 1749px; width: 608px; height: 603px; background: var(--panel); text-align: center; }
  .social { position: absolute; top: 46px; left: 0; width: 100%; display: flex; justify-content: center; gap: 44px; }
  .social-link { width: 52px; height: 52px; border: 2px solid #9a9a9a; border-radius: 8px; }
  .social-link.round { border-radius: 50%; }
  .footer-rule { position: absolute; top: 128px; left: 82px; width: 434px; height: 1px; background: var(--line); }
  .footer-brand { position: absolute; top: 188px; left: 178px; width: 252px; }
  .footer-brand .brand-name { color: #8a8a8a; font-weight: 300; }
  .contact { position: absolute; top: 266px; width: 100%; list-style: none; font-size: 20px; line-height: 37px; color: var(--grey-text); font-weight: 400; }
  .contact .phone { color: #222; }
  .footer-bottom { position: absolute; top: 509px; left: 0; width: 100%; border-top: 1px solid var(--line); padding-top: 36px; font-size: 15px; color: #8a8a8a; }
</style>
</head>
<body>
  <header class="site-header">
    <div class="brand">
      <span class="brand-name">TALLPINE</span>
    </div>
    <div class="menu-toggle" aria-label="Menu"><span></span><span></span><span></span></div>
  </header>

  <section class="hero">
    <div class="hero-art" role="img" aria-label="Illustration of a consultant pointing at a rising yearly growth line"></div>
    <h1 class="hero-title">WHAT IS<br>TALLPINE ?</h1>
    <a class="btn-learn">Learn more</a>
    <svg class="hero-edge" width="608" height="96" viewBox="0 0 608 96">
      <polygon points="0,96 608,14 608,96" fill="#fff"/>
      <polygon points="0,96 608,0 608,42" fill="#6a9a1f"/>
    </svg>
  </section>

  <section class="drivers-intro">
    <h2 class="drivers-title">WHY BUSINESS&nbsp; DRIVERS ?</h2>
    <p class="drivers-text">Tallpine facility upkeep systems is a boutique<br>firm specializing in maintenance and reliability,</p>
  </section>

  <ul class="driver-list">
    <li class="driver driver--planned">
      <div class="driver-icon" role="img" aria-label="Maintenance tools icon"></div>
      <span class="driver-label">Planned &amp;<br>Scheduled Maintenance</span>
    </li>
    <li class="driver driver--safety">
      <div class="driver-icon" role="img" aria-label="Safety shield icon"></div>
      <span class="driver-label">Longevity &amp;<br>Safety&nbsp; of Equipment</span>
    </li>
    <li class="driver driver--savings">
      <div class="driver-icon" role="img" aria-label="Savings chart icon"></div>
      <span class="driver-label">Administrative<br>Savings</span>
    </li>
    <li class="driver driver--uptime">
      <div class="driver-icon" role="img" aria-label="Performance monitor icon"></div>
      <span class="driver-label">Uptime<br>Improvements</span>
    </li>
    <li class="driver driver--assets">
      <div class="driver-icon" role="img" aria-label="Asset inspection icon"></div>
      <span class="driver-label">Optimized<br>Asset Performance</span>
    </li>
    <li class="driver driver--inventory">
      <div class="driver-icon" role="img" aria-label="Inventory files icon"></div>
      <span class="driver-label">Improved<br>Inventory Levels</span>
    </li>
  </ul>

  <footer class="site-footer">
    <div class="social">
      <a class="social-link" aria-label="Social link"></a>
      <a class="social-link round" aria-label="Social link"></a>
      <a class="social-link" aria-label="Social link"></a>
    </div>
    <div class="footer-rule"></div>
    <div class="footer-brand">
      <span class="brand-name">TALLPINE</span>
    </div>
    <ul class="contact">
      <li class="phone">604-555-0142</li>
      <li>info@tallpineupkeep.com</li>
      <li>Your address goes here</li>
      <li>Street Name</li>
      <li>Country</li>
      <li>Mon-Fri 7:00AM to 6:00PM</li>
    </ul>
    <div class="footer-bottom">© 2017 tallpineupkeep.com &nbsp; | &nbsp;All rights reserved</div>
  </footer>
</body>
</html>
```